Ferncastle Holdings - stationery for luxury, exclusive property investment company

We need stationery (letterhead, folder, compliments slip and envelope) and business cards which will reflect our luxury brand.

I have attached some design examples that we like.

We are an investment company which buys property to provide accommodation for corporate customers.

The design of the stationery needs to be be simple, refined, understated, luxury and very tasteful.

The design should communicate luxury and exclusivity, without being ostentatious.

Logo files are attached

Please can designers re-read the brief, and make sure the logo is in gold on either on a navy or white background.

Target Market(s)

Wealthy customers

Contact Information for Business Card

Helen Travers-Booth
Director
Ferncastle Holdings Limited
email: helen@ferncastleholdings.co.uk
mob: 07712645930

Font styles to use
Serif

Colors

Designer to choose colors to be used in the design.

Requirements
Must have
• The logo must be gold on either a white or navy background as per the attached logos.
• The stationery MUST have the following information:
• Ferncastle Holdings Limited
• The Willows
• Ashby Rise
• Ashby
• GL52 7TN
• Company Number: 20418736 (Registered in England and Wales)
• The letterhead must also have the two attached logos for the PLG and the PLG accreditation scheme. They do not need to be large.
Nice to have
• A watermark, navy banding either top or bottom.
Should not have
• Anything that looks budget.

```html
<!DOCTYPE html>
<html lang="en">
<head>
<meta charset="utf-8">
<title>Ferncastle Holdings – Presentation Folder</title>
<link rel="stylesheet" href="https://fonts.googleapis.com/css2?family=Cinzel:wght@500&family=Kumbh+Sans:wght@400;500&display=swap">
<style>
  :root {
    --navy: #000333;
    --navy-fold: #0a0d45;
    --gold: #d2ad5e;
    --pocket-grey: #b2b4b3;
    --frame-grey: #9a9a9a;
    --label-ink: #1a1a1a;
    --paper: #ffffff;
  }
  html, body {
    margin: 0;
    padding: 0;
    overflow: hidden;
    background: var(--paper);
  }
  .sheet {
    position: relative;
    width: 1200px;
    height: 1200px;
    box-sizing: border-box;
    border: 1px solid var(--frame-grey);
    background: var(--paper);
    overflow: hidden;
  }
  .sheet-label {
    position: absolute;
    left: 34px;
    top: 62px;
    margin: 0;
    font-family: Arial, Helvetica, sans-serif;
    font-weight: 400;
    font-size: 48px;
    letter-spacing: 1px;
    color: var(--label-ink);
  }
  .folder-pocket {
    position: absolute;
    left: 29px;
    top: 899px;
    width: 569px;
    height: 181px;
  }
  .folder-panel {
    position: absolute;
    top: 145px;
    height: 756px;
    background: var(--navy);
  }
  .folder-panel--back {
    left: 29px;
    width: 568px;
    border-right: 1px solid var(--navy-fold);
  }
  .folder-panel--front {
    left: 597px;
    width: 569px;
  }
  .company-details {
    position: absolute;
    left: 15px;
    bottom: 18px;
    font-family: "Kumbh Sans", sans-serif;
    color: var(--gold);
    line-height: 1;
  }
  .company-details__name {
    margin: 0 0 9px;
    font-size: 16px;
    font-weight: 500;
  }
  .company-details__line {
    margin: 0 0 5px;
    font-size: 11.5px;
  }
  .company-details__line--small {
    font-size: 10px;
    margin-bottom: 4px;
  }
  .brand-mark {
    position: absolute;
    left: 0;
    right: 0;
    top: 250px;
    display: flex;
    flex-direction: column;
    align-items: center;
  }
  .brand-mark__circle {
    width: 120px;
    height: 120px;
    border-radius: 50%;
    border: 3px solid var(--gold);
    box-sizing: border-box;
    margin-bottom: 92px;
  }
  .brand-mark__name {
    margin: 0;
    font-family: "Cinzel", serif;
    font-weight: 500;
    font-size: 34px;
    letter-spacing: 2px;
    color: var(--gold);
    white-space: nowrap;
  }
</style>
</head>
<body>
  <main class="sheet">
    <h1 class="sheet-label">FOLDER</h1>

    <svg class="folder-pocket" viewBox="0 0 569 181" aria-hidden="true">
      <polygon points="0,0 569,0 455,181 0,181" fill="var(--pocket-grey)"/>
    </svg>

    <section class="folder-panel folder-panel--back">
      <address class="company-details" style="font-style:normal">
        <p class="company-details__name">Ferncastle Holdings Limited</p>
        <p class="company-details__line">The Willows , Ashby Rise, Ashby, GL52 7TN</p>
        <p class="company-details__line company-details__line--small">Company Number: 20418736 (Registered in England and Wales)</p>
        <p class="company-details__line company-details__line--small">info@ferncastleholdings.co.uk</p>
      </address>
    </section>

    <section class="folder-panel folder-panel--front">
      <div class="brand-mark">
        <div class="brand-mark__circle" aria-hidden="true"></div>
        <p class="brand-mark__name">FERNCASTLE HOLDINGS</p>
      </div>
    </section>
  </main>
</body>
</html>
```